8 Page Publishing/Entertainment Website Design

We need a slick, polished, professional looking fully mobile responsive website designed for the publishing / entertainment industry. It will contain 8 pages, including the Home page. The site is to be designed in pure HTML and CSS only and to be compatible with any type of server we put it on. Pages are *not* to be part of any template system, like WordPress or others like it. Pure HTML and CSS standalone pages only. No WordPress or Joomla, etc. Website to use our logo's colors of red/white throughout its design. Uploaded files contain a word DOC that outlines more of our needs and we have included our logo file. Please read the specifications in the Word Document attached. We have also included a PDF file with the website specs as well.

Target Market(s)

Authors and Screenwriters

Coding

Coded - Design and coding required

Number of Pages Required

5+ page

Colors
ec1f27
ffffff
f04a50
f59195

Requirements
Must have
• The site is to be designed in pure HTML and CSS only and to be compatible with any type of server we put it on. Pages are *not* to be part of any template system, like WordPress or others like it. Pure HTML and CSS standalone pages only. No WordPress or Joomla, etc. Website to use our logo's colors of red/white throughout its design. Uploaded files contain a word DOC that outlines more of our needs and we have included our logo file. Please read the specifications in the Word Document attached. We have also included a PDF file with the website specs as well.
Should not have
• No Wordpress or other Template type pages. Pure HTML and CSS only. Some Javascript and JQuery is okay, upon approval.

```html
<!DOCTYPE html>
<html lang="en">
<head>
<meta charset="utf-8">
<title>QHP – Publishing &amp; Entertainment</title>
<link href="https://fonts.googleapis.com/css2?family=Open+Sans:ital,wght@0,400;0,600;0,700;1,400&family=Poppins:wght@500;700&family=Playfair+Display:ital@1&display=swap" rel="stylesheet">
<style>
:root{
  --red:#ec1f27;
  --red-soft:#f04a50;
  --red-pale:#f59195;
  --white:#ffffff;
  --ink:#222222;
  --muted:#777777;
  --band:#c9c9c9;
  --light:#f1f1f1;
  --cta:#8a8a8a;
  --footer:#0b0b0b;
  --footer-bottom:#1a1a1a;
  --sky:#2aa6df;
}
*{margin:0;padding:0;box-sizing:border-box}
html,body{width:1200px;height:3774px;overflow:hidden}
body{position:relative;background:var(--white);font-family:"Open Sans",Arial,sans-serif;color:var(--ink)}
.abs{position:absolute}

/* top bar + header */
.topbar-links{left:244px;top:6px;font-size:9px;color:var(--muted);display:flex;gap:16px}
.topbar-account{left:868px;top:6px;font-size:9px;color:var(--muted);display:flex;gap:18px}
.topbar-rule{left:0;top:26px;width:1200px;height:1px;background:#e5e5e5}
.brand{left:70px;top:34px;display:flex;align-items:center;gap:10px}
.brand-mark{width:56px;height:56px;border-radius:50%;background:var(--red)}
.brand-name{font-weight:700;font-size:20px;color:var(--red)}
.main-nav{left:206px;top:61px;display:flex;gap:19px;font-weight:700;font-size:13px;color:var(--red);letter-spacing:.1px;white-space:nowrap}
.cart-icon{left:926px;top:59px}

/* hero */
.hero{left:0;top:100px;width:1200px;height:474px;background:linear-gradient(120deg,#d9d4cc 0%,#efece7 40%,#c9c3ba 70%,#8e8a84 100%)}
.hero-video{left:63px;top:171px;width:415px;height:307px;background:#000;border:4px solid var(--red)}
.hero-video svg{position:absolute;left:175px;top:110px}
.btn-red{background:var(--red);color:var(--white);font-weight:700;border-radius:6px;text-align:center}
.hero-apply{left:234px;top:503px;width:148px;height:45px;line-height:45px;font-size:17px;box-shadow:0 3px 6px rgba(0,0,0,.3)}

/* section band */
.band{left:0;width:1200px;background:var(--band)}
.band-title{width:1200px;text-align:center;color:var(--red);font-weight:700;font-size:22px}

/* feature rows */
.feature-title{color:var(--red);font-weight:700;font-size:15px}
.feature-text{font-size:13.5px;line-height:1.55;color:var(--ink)}
.feature-small{font-size:8.5px;line-height:1.55;color:var(--muted)}
.photo{border-radius:2px}

/* testimonials */
.testimonials{left:0;top:1610px;width:1200px;height:383px;background:var(--light)}
.testi-side{top:1680px;height:245px;background:#dedede}
.testi-card{left:372px;top:1660px;width:524px;height:290px;background:var(--white);box-shadow:0 2px 10px rgba(0,0,0,.12)}
.testi-heading{left:541px;top:1697px;font-family:Poppins,sans-serif;font-weight:500;font-size:16px;letter-spacing:1.5px;color:#333}
.testi-name{left:543px;top:1750px;font-family:Poppins,sans-serif;font-size:14px;letter-spacing:1.5px;color:#333}
.testi-role{left:543px;top:1772px;font-size:8px;letter-spacing:1.5px;color:#aaa}
.testi-quote{left:543px;top:1800px;width:300px;font-family:"Playfair Display",serif;font-style:italic;font-size:15px;line-height:1.55;color:#999}
.testi-arrow{width:24px;height:24px;background:var(--sky);top:1804px}
.testi-dots{left:586px;top:1926px;display:flex;gap:6px}
.testi-dots span{width:6px;height:6px;border-radius:50%;background:#ccc}

/* table of contents */
.toc{left:0;top:1993px;width:1200px;height:468px;background:linear-gradient(100deg,#6f6f6f 0%,#4b4b4b 40%,#3a3a3a 70%,#555 100%)}
.toc-title{left:252px;top:2066px;font-family:Poppins,sans-serif;font-weight:700;font-size:28px;color:var(--white)}
.toc-item{width:210px;color:var(--white)}
.toc-item h4{font-size:11.5px;font-weight:700;margin-bottom:6px}
.toc-item p{font-size:10.5px;line-height:1.55;color:#e6e6e6}
.toc-btn{left:521px;top:2375px;background:#222;color:var(--white);font-size:9px;padding:6px 10px;letter-spacing:.5px}

/* authors */
.author-photo{top:2574px;width:212px;height:158px}
.author-name{top:2734px;color:var(--red);font-size:17px}
.author-role{top:2757px;color:var(--red);font-size:13px}
.author-social{top:2783px;display:flex;gap:10px}
.author-social span{width:7px;height:7px;border-radius:50%;background:#666}

/* risk free */
.risk-title{left:264px;top:2843px;font-weight:700;font-size:17px}
.risk-sub{left:264px;top:2886px;font-weight:700;font-size:11px}
.risk-text{left:264px;top:2918px;width:540px;font-weight:700;font-size:11px;line-height:1.5}
.risk-seal{left:893px;top:2845px;width:134px;height:124px;border-radius:50%;background:#1b3561;border:6px solid #c8a44a}

/* partners */
.partners{left:8px;top:2994px;width:1184px;height:118px;background:var(--red)}
.partner{top:3021px;width:112px;height:78px;background:var(--white);border:1px solid #ddd}

/* call to action */
.cta{left:0;top:3143px;width:1200px;height:274px;background:var(--cta)}
.cta-title{left:0;top:3154px;width:1200px;text-align:center;color:var(--white);font-weight:700;font-size:21px}
.cta-btn{left:428px;top:3321px;width:259px;height:76px;line-height:76px;border-radius:10px;background:#c7c7c7;color:var(--red);font-weight:700;font-size:22px;text-align:center}

/* footer */
.footer{left:0;top:3417px;width:1200px;height:231px;background:var(--footer)}
.footer-head{top:3432px;color:var(--red);font-weight:700;font-size:17px}
.footer-text{color:#ddd;font-size:9px;line-height:1.55}
.footer-link{color:var(--sky)}
.info-list{left:584px;top:3478px;width:190px}
.info-list div{display:flex;justify-content:space-between;font-size:9px;color:#ddd;border-bottom:1px solid #333;height:28px;align-items:center}
.news-line{display:flex;gap:8px;align-items:center;margin-top:8px}
.email-field{left:794px;top:3545px;width:168px;height:22px;background:#2a2a2a;color:#999;font-size:9px;padding:5px 8px}
.subscribe{left:794px;top:3577px;width:58px;height:20px;line-height:20px;text-align:center;background:var(--sky);color:var(--white);font-size:8px;font-weight:700}
.bottom-bar{left:0;top:3648px;width:1200px;height:126px;background:var(--footer-bottom)}
.copyright{left:244px;top:3681px;font-size:9px;color:#ccc}
.pay{top:3676px;width:34px;height:22px;border-radius:3px;background:#d8d8d8}
</style>
</head>
<body>

<!-- top bar -->
<div class="abs topbar-links"><span>HOME</span><span>ABOUT US</span><span>CONTACT US</span><span>BUY THEME</span></div>
<div class="abs topbar-account"><span>ENG</span><span>MY ACCOUNT</span></div>
<div class="abs topbar-rule"></div>

<!-- header -->
<div class="abs brand"><span class="brand-mark"></span><span class="brand-name">QHP</span></div>
<nav class="abs main-nav"><span>HOME</span><span>ABOUT QHP</span><span>APPLY NOW</span><span>QHP WORLDS</span><span>QHP AUTHORS</span><span>FAQ</span><span>NEWS</span><span>CONTACT US</span></nav>
<svg class="abs cart-icon" width="20" height="20" viewBox="0 0 20 20"><path d="M2 3h3l2 9h9l2-7H6" fill="none" stroke="#555" stroke-width="2"/><circle cx="8" cy="16" r="1.6" fill="#555"/><circle cx="15" cy="16" r="1.6" fill="#555"/></svg>

<!-- hero -->
<div class="abs hero" role="img" aria-label="Photo of hands using a tablet showing an e-book library on a desk"></div>
<div class="abs hero-video"><svg width="70" height="70" viewBox="0 0 70 70"><path d="M8 5 L64 35 L8 65 Z" fill="none" stroke="#ec1f27" stroke-width="6"/></svg></div>
<div class="abs btn-red hero-apply">Apply Now</div>

<!-- about band -->
<div class="abs band" style="top:574px;height:110px"></div>
<div class="abs band-title" style="top:612px">About QHP</div>

<!-- about row -->
<div class="abs feature-title" style="left:164px;top:731px">About QHP</div>
<p class="abs feature-text" style="left:164px;top:793px;width:440px">Page will feature company information at the top, then another section below it featuring alternating (left/right) photo and background information and accomplishments for the two founders of the company. Both are men.</p>
<div class="abs photo" style="left:616px;top:694px;width:546px;height:277px;background:linear-gradient(135deg,#f4f4f4,#9a9a9a 50%,#e9e9e9)" role="img" aria-label="Photo of a folding tablet showing a news page"></div>

<!-- apply row -->
<div class="abs photo" style="left:93px;top:1011px;width:440px;height:259px;background:linear-gradient(135deg,#eef0f4,#c7ccd6 50%,#e04048 75%,#dfe3ea)" role="img" aria-label="Photo of a keyboard with a red publish key"></div>
<div class="abs feature-title" style="left:609px;top:1045px">Apply Now</div>
<p class="abs feature-small" style="left:609px;top:1068px;width:553px">Send us your manuscript or screenplay and our editors will review every page with care. We read each entry within weeks and reply with notes, next steps and an honest view of where the work fits. Writers of all genres are welcome to apply, from first novels to series.</p>
<p class="abs feature-small" style="left:609px;top:1128px;width:553px">Share a short synopsis, a sample chapter and a few lines about yourself. Our team will guide you through editing, design, print and screen rights so your story reaches its readers.</p>

<!-- worlds row -->
<div class="abs feature-title" style="left:168px;top:1352px">QHP WORLDS</div>
<p class="abs feature-text" style="left:168px;top:1402px;width:430px">Page will feature three worlds (sections) listed one after another. Each world/section will contain a large image that represents one of our book worlds with description text below it. This page</p>
<div class="abs photo" style="left:692px;top:1296px;width:440px;height:289px;background:radial-gradient(ellipse at center,#e8d9b8 0%,#f3efe6 55%,#ffffff 100%)" role="img" aria-label="Illustration of a reader surrounded by stacks of books"></div>

<!-- testimonials -->
<div class="abs testimonials"></div>
<div class="abs band-title" style="top:1620px;font-size:17px">Testimonials</div>
<div class="abs testi-side" style="left:252px;width:130px"></div>
<div class="abs testi-side" style="left:886px;width:70px"></div>
<div class="abs testi-card"></div>
<svg class="abs" style="left:512px;top:1692px" width="24" height="22" viewBox="0 0 24 22"><rect x="1" y="3" width="16" height="14" fill="none" stroke="#9ac" stroke-width="1.5"/><rect x="6" y="1" width="16" height="14" fill="none" stroke="#9ac" stroke-width="1.5"/></svg>
<div class="abs testi-heading">WHAT PEOPLE SAY</div>
<div class="abs" style="left:365px;top:1754px;width:163px;height:133px;background:linear-gradient(160deg,#d6d6d6,#8d8d8d)" role="img" aria-label="Portrait of the reviewer"></div>
<div class="abs testi-name">EVAN MARLOW</div>
<div class="abs testi-role">AUTHOR AT QHP</div>
<p class="abs testi-quote">"The team made my first novel real, from edits and cover to launch day. Clear advice, kind notes, and a book I am proud to share."</p>
<div class="abs testi-arrow" style="left:286px"><svg width="24" height="24" viewBox="0 0 24 24"><path d="M14 7l-5 5 5 5" fill="none" stroke="#fff" stroke-width="2"/></svg></div>
<div class="abs testi-arrow" style="left:886px"><svg width="24" height="24" viewBox="0 0 24 24"><path d="M10 7l5 5-5 5" fill="none" stroke="#fff" stroke-width="2"/></svg></div>
<div class="abs testi-dots"><span></span><span style="background:#999"></span><span></span></div>

<!-- table of contents -->
<div class="abs toc" role="img" aria-label="Dark photo of an office with shelves of books"></div>
<div class="abs toc-title">TABLE OF CONTENTS</div>
<div class="abs toc-item" style="left:252px;top:2140px"><h4>Introduction</h4><p>Voluptate velit esse quam molestiae consequatur vel illum qui dolorem fugiat quo voluptas pariatur placeat ullamco.</p></div>
<div class="abs toc-item" style="left:486px;top:2140px"><h4>Business Experience</h4><p>Voluptate velit esse quam molestiae consequatur vel illum qui dolorem fugiat quo voluptas pariatur placeat ullamco.</p></div>
<div class="abs toc-item" style="left:722px;top:2140px"><h4>Measuring Technique</h4><p>Voluptate velit esse quam molestiae consequatur vel illum qui dolorem fugiat quo voluptas pariatur placeat ullamco.</p></div>
<div class="abs toc-item" style="left:252px;top:2258px"><h4>User Research</h4><p>Voluptate velit esse quam molestiae consequatur vel illum qui dolorem fugiat quo voluptas pariatur placeat ullamco.</p></div>
<div class="abs toc-item" style="left:486px;top:2258px"><h4>Appendix</h4><p>Voluptate velit esse quam molestiae consequatur vel illum qui dolorem fugiat quo voluptas pariatur placeat ullamco.</p></div>
<div class="abs toc-item" style="left:722px;top:2258px"><h4>Validating Ideas</h4><p>Voluptate velit esse quam molestiae consequatur vel illum qui dolorem fugiat quo voluptas pariatur placeat ullamco.</p></div>
<div class="abs toc-btn">GET A FREE SAMPLE ›</div>

<!-- authors -->
<div class="abs band-title" style="top:2502px;font-size:18px">Authors</div>
<div class="abs author-photo" style="left:264px;background:linear-gradient(160deg,#e0e0e0,#8a8a8a)" role="img" aria-label="Portrait of author"></div>
<div class="abs author-photo" style="left:493px;background:linear-gradient(160deg,#f0f0f0,#9a8f86)" role="img" aria-label="Portrait of author"></div>
<div class="abs author-photo" style="left:722px;background:linear-gradient(160deg,#c9cdd2,#6b6f74)" role="img" aria-label="Portrait of author"></div>
<div class="abs author-name" style="left:264px">John Doe</div><div class="abs author-role" style="left:264px">Seasoned Writer</div>
<div class="abs author-name" style="left:493px">John Doe</div><div class="abs author-role" style="left:493px">Seasoned Writer</div>
<div class="abs author-name" style="left:722px">John Doe</div><div class="abs author-role" style="left:722px">Seasoned Writer</div>
<div class="abs author-social" style="left:264px"><span></span><span></span><span></span><span></span></div>
<div class="abs author-social" style="left:493px"><span></span><span></span><span></span><span></span></div>
<div class="abs author-social" style="left:722px"><span></span><span></span><span></span><span></span></div>

<!-- risk free -->
<div class="abs band" style="top:2836px;height:141px"></div>
<div class="abs risk-title">RISK FREE</div>
<div class="abs risk-sub">60 Days Money Back Guarantee</div>
<p class="abs risk-text">If for any reason you are not completely satisfied with our services, simply contact us within 30 Days from purchase, and we'll quickly process your refund. No questions asked!</p>
<div class="abs risk-seal"></div>

<!-- partners -->
<div class="abs partners"></div>
<div class="abs partner" style="left:271px"></div>
<div class="abs partner" style="left:407px"></div>
<div class="abs partner" style="left:536px"></div>
<div class="abs partner" style="left:656px"></div>
<div class="abs partner" style="left:783px"></div>

<!-- call to action -->
<div class="abs cta"></div>
<div class="abs cta-title">Ready To Start Selling More Books</div>
<div class="abs cta-btn">Sign Up Now</div>

<!-- footer -->
<div class="abs footer"></div>
<div class="abs footer-head" style="left:239px">Latest News</div>
<div class="abs footer-head" style="left:415px">About Us</div>
<div class="abs footer-head" style="left:584px">Information</div>
<div class="abs footer-head" style="left:730px">Contact Us</div>

<div class="abs footer-text" style="left:239px;top:3472px;width:160px">
  <p>Fresh titles, author events and release dates from our team, posted every week.</p>
  <div class="news-line"><svg width="9" height="11" viewBox="0 0 9 11"><path d="M4.5 10S1 6 1 4a3.5 3.5 0 017 0c0 2-3.5 6-3.5 6z" fill="#ddd"/></svg><span>88 Maple Row, 4th floor, Ashford</span></div>
  <div class="news-line"><svg width="9" height="9" viewBox="0 0 9 9"><path d="M1 1h2l1 2-1 1a5 5 0 002 2l1-1 2 1v2a1 1 0 01-1 1A7 7 0 010 2a1 1 0 011-1z" fill="#ddd"/></svg><span>+(555) 014 2280</span></div>
  <div class="news-line"><svg width="10" height="8" viewBox="0 0 10 8"><rect x=".5" y=".5" width="9" height="7" fill="none" stroke="#ddd"/><path d="M.5 .5l4.5 4 4.5-4" fill="none" stroke="#ddd"/></svg><span>hello@qhpbooks.com</span></div>
</div>

<div class="abs footer-text" style="left:430px;top:3472px;width:140px">
  <p>New author interviews are live on the blog this week from <span class="footer-link">@qhpress</span></p>
  <p style="margin-top:12px">Our spring reading list is out now, see it at <span class="footer-link">@qhpress</span> today</p>
</div>

<div class="abs info-list">
  <div><span>Specials</span><span>›</span></div>
  <div><span>New Products</span><span>›</span></div>
  <div><span>Best Sellers</span><span>›</span></div>
  <div><span>Contact Us</span><span>›</span></div>
  <div><span>Terms of Use</span><span>›</span></div>
  <div><span>Site Map</span><span>›</span></div>
</div>

<p class="abs footer-text" style="left:794px;top:3472px;width:170px">Join our list for release news, writing tips and open calls for new work.</p>
<div class="abs email-field">E-mail</div>
<div class="abs subscribe">SUBSCRIBE</div>

<div class="abs bottom-bar"></div>
<div class="abs copyright">Copyrights © 2016 Quillhouse. All rights reserved</div>
<div class="abs pay" style="left:795px"></div>
<div class="abs pay" style="left:835px"></div>
<div class="abs pay" style="left:875px"></div>
<div class="abs pay" style="left:915px"></div>

</body>
</html>
```